Need Help having my business card stand out

I am the owner of Pine Ridge Canine Coaching and would like for my business cards to stand out. I have been trying to keep designing them myself but I can't get what I have in my head on the card. I will try my best to post templates that I like for inspirations. I want something unique but elegant. I don't want in to look cartoony or cheesy. It needs to pop in a pet shop but also in a coffee shop or gym.

Target Market(s)

Dog owners, Married ,No young kids Jr High school kids and up (maybe kids on the way) Executives, Stay at home moms/wives, Small business owners

Industry/Entity Type

Dog Training

Contact Information for Business Card

Trevor Holloway, 555-304-7162, info@pineridgecanine.example, www.pineridgecanine.example

Colors

Designer to choose colors to be used in the design.

Requirements
Must have
• my logo
Should not have
• Cursive lettering

```html
<!DOCTYPE html>
<html lang="en">
<head>
<meta charset="utf-8">
<title>Pine Ridge Canine Coaching – Business Card</title>
<link rel="stylesheet" href="https://fonts.googleapis.com/css2?family=Roboto:wght@400;500&display=swap">
<style>
  :root {
    --backdrop: #c6c6c8;
    --card-dark: #000000;
    --card-light: #f4f4f4;
    --ink-light: #ffffff;
    --ink-soft: #e6e6e6;
    --ink-dark: #1c1c1c;
    --icon-box: #3a3a3a;
    --grass: #4f6b3a;
    --shade: #2c3a22;
    --foliage: #8a8f5a;
  }
  * { margin: 0; padding: 0; box-sizing: border-box; }
  html, body { width: 1200px; height: 1200px; overflow: hidden; }
  body {
    background: var(--backdrop);
    font-family: "Roboto", Arial, sans-serif;
    position: relative;
  }
  .card {
    position: absolute;
    width: 700px;
    height: 400px;
    overflow: hidden;
  }
  .card--front { left: 250px; top: 150px; background: var(--card-dark); }
  .card--back { left: 250px; top: 630px; background: var(--card-light); }

  .front-photo { position: absolute; left: 0; top: 0; }

  .brand {
    position: absolute;
    display: flex;
    align-items: center;
    gap: 12px;
    font-weight: 500;
    line-height: 1.2;
  }
  .brand__mark {
    width: 34px; height: 34px;
    border-radius: 50%;
    flex: none;
  }
  .brand__name { font-size: 22px; }

  .card--front .brand {
    right: 30px; top: 95px;
    color: var(--ink-light);
    text-align: right;
  }
  .card--front .brand__mark { border: 2px solid var(--ink-light); }

  .holder-name {
    position: absolute;
    right: 28px; top: 222px;
    color: var(--ink-light);
    font-size: 25px;
    font-weight: 500;
    letter-spacing: 0.5px;
  }
  .contact {
    position: absolute;
    right: 28px;
    list-style: none;
    color: var(--ink-soft);
    font-size: 18px;
  }
  .contact li {
    display: flex;
    justify-content: flex-end;
    align-items: center;
    gap: 12px;
    height: 24px;
  }
  .contact__icon {
    width: 17px; height: 17px;
    background: var(--icon-box);
    display: flex; align-items: center; justify-content: center;
  }
  .contact--phone { top: 276px; }
  .contact--web { top: 318px; }
  .contact--web li + li { margin-top: 6px; }

  .card--back .brand {
    left: 48px; top: 260px;
    color: var(--ink-dark);
  }
  .card--back .brand__mark { background: var(--ink-dark); }
  .card--back .brand__name { font-size: 20px; }
  .back-url {
    position: absolute;
    left: 46px; top: 332px;
    color: var(--ink-dark);
    font-size: 19px;
    letter-spacing: 0.3px;
  }
</style>
</head>
<body>

<section class="card card--front">
  <svg class="front-photo" width="700" height="400" viewBox="0 0 700 400" role="img" aria-label="Photo of a trainer working with three dogs on a grassy park lawn">
    <defs>
      <linearGradient id="parkTones" x1="0" y1="0" x2="0" y2="1">
        <stop offset="0" stop-color="var(--foliage)"/>
        <stop offset="0.35" stop-color="var(--grass)"/>
        <stop offset="1" stop-color="var(--shade)"/>
      </linearGradient>
    </defs>
    <path d="M0 0 H298 Q345 190 212 400 H0 Z" fill="url(#parkTones)"/>
    <path d="M298 0 Q345 190 212 400" fill="none" stroke="var(--ink-soft)" stroke-width="4"/>
  </svg>

  <div class="brand">
    <span class="brand__name">Pine Ridge<br>Canine Coaching</span>
    <span class="brand__mark"></span>
  </div>

  <h1 class="holder-name">TREVOR HOLLOWAY</h1>

  <ul class="contact contact--phone">
    <li>555-304-7162
      <span class="contact__icon">
        <svg width="11" height="11" viewBox="0 0 24 24"><path d="M6.6 10.8a15 15 0 0 0 6.6 6.6l2.2-2.2a1 1 0 0 1 1-.25 11.4 11.4 0 0 0 3.6.57 1 1 0 0 1 1 1V20a1 1 0 0 1-1 1A17 17 0 0 1 3 4a1 1 0 0 1 1-1h3.5a1 1 0 0 1 1 1c0 1.25.2 2.45.57 3.57a1 1 0 0 1-.25 1z" fill="#111"/></svg>
      </span>
    </li>
  </ul>

  <ul class="contact contact--web">
    <li>info@pineridgecanine.example
      <span class="contact__icon">
        <svg width="11" height="9" viewBox="0 0 22 16"><rect x="1" y="1" width="20" height="14" fill="none" stroke="#111" stroke-width="2"/><path d="M1 1 L11 9 L21 1" fill="none" stroke="#111" stroke-width="2"/></svg>
      </span>
    </li>
    <li>www.pineridgecanine.example
      <span class="contact__icon">
        <svg width="11" height="11" viewBox="0 0 20 20"><circle cx="10" cy="10" r="8" fill="none" stroke="#111" stroke-width="2"/><path d="M2 10 H18 M10 2 Q5 10 10 18 Q15 10 10 2" fill="none" stroke="#111" stroke-width="1.5"/></svg>
      </span>
    </li>
  </ul>
</section>

<section class="card card--back">
  <div class="brand">
    <span class="brand__mark"></span>
    <span class="brand__name">Pine Ridge<br>Canine Coaching</span>
  </div>
  <p class="back-url">www.pineridgecanine.example</p>
</section>

</body>
</html>
```